Create a Graphic About YOURSELF and PixelHarbor

PixelHarbor would like you (designers) to create an awesome graphic to promote YOURSELF and your profile on PixelHarbor!

Your graphic should communicate your name, your services and should mention PixelHarbor.

The design should be perfect for sharing on Chatterly. Here's an example of what we'd like http://blog.pixelharbor-example.ca/article/333/pixelharbor-launches-3000-hire-me-social-design-contest

Once you submitted your design, we'd love you to share the design ('advertisement') and promote yourself and PixelHarbor to your friends and potential customers. So make your submissions great and get your friends to vote for your design by 'Liking' it on Chatterly!

Prizes:
$1500 - "PixelHarbor Community" prize awarded to the designer with the most Chatterly 'Likes'
5 x $50 for the next 5 'most liked' designs on Chatterly

$1000 - "Hire Me" prize awarded to the designer who receives the most client invites
5 x $50 for the next 5 'most invited' designers

In summary, this is a great opportunity for you to increase your exposure to PixelHarbor customers and win cash prizes. Show off your design skills and get hired by PixelHarbor customers from around the world!

Target Market(s)

Fans, friends and customers of YOU

Industry/Entity Type

Cash

Requirements
Must have
• 1) Include your PixelHarbor user name on the graphic so customers can find you in the PixelHarbor Designer Directory
2) Include the tagline "Hire Me on PixelHarbor.com!" in your graphic design.
3) Share your design's URL on our Chatterly wall at http://chatterly-example.com/pixelharbor and get your friends to 'like' your design.
Nice to have
• 1) Include a tagline that expresses your design approach/philosophy
2) Artwork dimensions: 403 x 403 px
3) You can submit more than 1 design!
Should not have
• You must own the copyright of any images you use including stock imagery.

```html
<!DOCTYPE html>
<html lang="en">
<head>
<meta charset="utf-8">
<title>Jonah Brandt – Hire Me on PixelHarbor.com!</title>
<link rel="stylesheet" href="https://fonts.googleapis.com/css2?family=Open+Sans:wght@300;400;700;800&display=swap">
<style>
  :root {
    --bg-center: #3a3a3d;
    --bg-edge: #141416;
    --yellow: #f7b81c;
    --cyan: #1cc6e8;
    --green: #7dc51f;
    --white: #ffffff;
    --magenta: #e8269b;
  }
  html, body {
    margin: 0;
    padding: 0;
    width: 1200px;
    height: 1200px;
    overflow: hidden;
    background: var(--bg-edge);
  }
  .promo-canvas {
    display: block;
    width: 1200px;
    height: 1200px;
    font-family: "Open Sans", Arial, sans-serif;
  }
  .name-bold { font-weight: 800; fill: var(--yellow); }
  .name-light { font-weight: 300; fill: var(--yellow); }
  .tagline { font-weight: 400; fill: var(--white); }
  .tagline-strong { font-weight: 700; }
  .service { font-weight: 400; fill: var(--white); }
  .service-strong { font-weight: 700; fill: var(--white); }
  .service-accent { font-weight: 700; fill: var(--green); }
  .service-divider { font-weight: 300; fill: var(--green); }
  .service-more { font-weight: 400; fill: var(--cyan); }
  .service-more-strong { font-weight: 700; fill: var(--cyan); }
  .hire-line { font-weight: 400; fill: var(--white); }
  .hire-site { font-weight: 800; fill: var(--white); }
  .band-yellow { fill: var(--yellow); }
  .band-cyan { fill: var(--cyan); }
</style>
</head>
<body>
<svg class="promo-canvas" viewBox="0 0 1200 1200" xmlns="http://www.w3.org/2000/svg">
  <defs>
    <radialGradient id="bg-glow" cx="50%" cy="45%" r="75%">
      <stop offset="0" stop-color="var(--bg-center)"/>
      <stop offset="1" stop-color="var(--bg-edge)"/>
    </radialGradient>
    <radialGradient id="cyan-soft" cx="35%" cy="30%" r="65%">
      <stop offset="0" stop-color="var(--cyan)" stop-opacity="0.85"/>
      <stop offset="1" stop-color="var(--cyan)" stop-opacity="0"/>
    </radialGradient>
    <radialGradient id="yellow-soft" cx="65%" cy="65%" r="65%">
      <stop offset="0" stop-color="var(--yellow)" stop-opacity="0.85"/>
      <stop offset="1" stop-color="var(--yellow)" stop-opacity="0"/>
    </radialGradient>
    <linearGradient id="confetti-soft" x1="0" y1="0" x2="1" y2="1">
      <stop offset="0" stop-color="var(--magenta)" stop-opacity="0.3"/>
      <stop offset="0.5" stop-color="var(--cyan)" stop-opacity="0.25"/>
      <stop offset="1" stop-color="var(--yellow)" stop-opacity="0.25"/>
    </linearGradient>
  </defs>

  <rect class="background" width="1200" height="1200" fill="url(#bg-glow)"/>

  <rect class="figure-top-left" x="0" y="0" width="360" height="300" fill="url(#cyan-soft)"
        role="img" aria-label="Cyan group-of-people emblem, corner decoration"/>
  <polygon class="confetti-burst" points="870,40 940,40 940,200 890,330 690,420 680,370"
           fill="url(#confetti-soft)"
           role="img" aria-label="Scattered triangle confetti in magenta, cyan and yellow"/>
  <rect class="figure-bottom-right" x="830" y="980" width="370" height="220" fill="url(#yellow-soft)"
        role="img" aria-label="Yellow group-of-people emblem, corner decoration"/>

  <g class="bands-right">
    <polygon class="band-yellow" points="700,500 1050,305 1056,318 706,512"/>
    <polygon class="band-yellow" points="1050,305 1085,292 1040,800 985,825"/>
    <polygon class="band-cyan" points="1140,560 1200,528 1200,560 1168,578"/>
    <polygon class="band-cyan" points="1115,705 1200,660 1200,692 1145,722"/>
  </g>

  <g class="bands-bottom-left">
    <polygon class="band-yellow" points="60,1075 445,842 451,854 66,1087"/>
    <polygon class="band-yellow" points="0,1010 390,870 430,855 0,1045"/>
    <polygon class="band-cyan" points="0,1115 150,1055 165,1065 0,1140"/>
    <polygon class="band-yellow" points="60,1200 300,1060 330,1060 110,1200"/>
  </g>

  <g class="identity" transform="rotate(-27 75 495)">
    <text x="75" y="495" font-size="104">
      <tspan class="name-bold">JONAH</tspan><tspan class="name-light"> BRANDT</tspan>
    </text>
    <text class="tagline" x="95" y="562" font-size="50">
      YOU <tspan class="tagline-strong">IMAGINE</tspan>... I <tspan class="tagline-strong">DESIGN</tspan>
    </text>
  </g>

  <g class="services" transform="rotate(-28 470 640)">
    <text class="service" x="470" y="640" font-size="74">LOGO</text>
    <text x="452" y="718" font-size="74" text-anchor="end">
      <tspan class="service-divider">|</tspan><tspan class="service-accent" dx="22">DESIGN</tspan>
    </text>
    <text class="service-strong" x="470" y="718" font-size="74">WEBSITE</text>
    <text class="service" x="470" y="796" font-size="74">BROCHURE</text>
    <text class="service" x="470" y="874" font-size="74">STATIONARY</text>
    <text x="470" y="934" font-size="48">
      <tspan class="service-more">and </tspan><tspan class="service-more-strong">many more</tspan>
    </text>
  </g>

  <g class="hire-me" transform="rotate(-27 590 1065)">
    <text class="hire-line" x="590" y="1065" font-size="46">HIRE ME ON</text>
    <text class="hire-site" x="590" y="1120" font-size="50">PIXELHARBOR.COM!</text>
  </g>
</svg>
</body>
</html>
```